Commerical Office Furniture Company Needs Truck Wrap Design for Box Truck

We need a truck wrap design (and business card) for our company based in Fresno, California. We offer commercial office furnishings such as private office desks, cubicle stations, conference tables, all office seating (task chairs, guest, lobby/lounge, conference) storage systems, ergonomic solutions (monitor arms, keyboard trays, lift desks) and much more. We are a full service office furniture dealer who can fully outfit every space and need for a new or existing office space. We also offer design and space planning services and professional installation.
We would like our trap wrap to be modern using the same color scheme as our logo with a clean but eye catching look. Perhaps using a few nice looking desk/workstations product images as examples to show people what we are capable of. We attached some examples of some themes/layouts we like. feel free to be creative. Our website tembrolight.com has some images and info.
https://imagelibrary.brv-corp.com/detail/client-space-shared-prism-workstation-with-t-line-storage-height-adjustable-tables-and-dorval-seating
Target Market(s)
Private Sector, Education, Healthcare
Industry/Entity Type
Requirements
Must have
- Varto Box Truck - 190 inches x 85 inches

```html
<!DOCTYPE html>
<html lang="en">
<head>
<meta charset="utf-8">
<title>Tembrolight Office Interiors – Box Truck Wrap</title>
<link href="https://fonts.googleapis.com/css2?family=Poppins:wght@500;600;700&display=swap" rel="stylesheet">
<style>
  :root {
    --brand-blue: #1652d6;
    --charcoal: #3a3c41;
    --ink: #3b3d42;
    --panel-light: #ebecee;
    --page: #f4f4f5;
    --white: #ffffff;
  }
  html, body {
    margin: 0;
    width: 1200px;
    height: 1200px;
    overflow: hidden;
    background: var(--page);
    font-family: "Poppins", sans-serif;
  }
  .sheet {
    width: 1200px;
    height: 1200px;
    display: flex;
    flex-direction: column;
    justify-content: space-evenly;
    align-items: center;
  }
  .wrap-panel {
    display: block;
    width: 1100px;
    height: 492px;
    box-shadow: 0 2px 10px rgba(0,0,0,0.12);
  }
  .phone { font-weight: 600; letter-spacing: 3px; }
  .web { font-weight: 500; letter-spacing: 1.5px; }
  .brand-name { font-weight: 700; fill: var(--brand-blue); }
  .tagline { font-weight: 500; fill: var(--ink); }
</style>
</head>
<body>
<main class="sheet">

  <!-- Concept A: circular showcase -->
  <svg class="wrap-panel" viewBox="0 0 1100 492" xmlns="http://www.w3.org/2000/svg">
    <defs>
      <linearGradient id="roomA" x1="0" y1="0" x2="0" y2="1">
        <stop offset="0" stop-color="#e4e2de"/>
        <stop offset="0.55" stop-color="#d6d0c6"/>
        <stop offset="1" stop-color="#b9a78e"/>
      </linearGradient>
      <clipPath id="circleClip"><circle cx="826" cy="244" r="218"/></clipPath>
    </defs>
    <rect class="panel-bg" width="1100" height="492" fill="var(--panel-light)"/>
    <rect class="dark-field" x="600" y="0" width="500" height="492" fill="var(--charcoal)"/>
    <rect class="contact-band" x="0" y="16" width="660" height="96" fill="var(--brand-blue)"/>
    <text class="phone" x="106" y="68" font-size="44" fill="var(--white)">555-014-2760</text>
    <text class="web" x="106" y="100" font-size="25" fill="var(--white)">www.tembrolight.com</text>

    <text class="brand-name" x="48" y="230" font-size="66">TEMBROLIGHT</text>
    <text class="brand-name" x="50" y="300" font-size="44">OFFICE INTERIORS</text>
    <text class="tagline" x="50" y="372" font-size="21">Office Furniture  •  Design  •  Installation</text>

    <g role="img" aria-label="Photo of a conference room with a wooden table and office chairs">
      <rect x="600" y="20" width="460" height="460" fill="url(#roomA)" clip-path="url(#circleClip)"/>
    </g>
    <circle class="showcase-ring" cx="826" cy="244" r="225" fill="none" stroke="var(--brand-blue)" stroke-width="16"/>
  </svg>

  <!-- Concept B: angled photo bands -->
  <svg class="wrap-panel" viewBox="0 0 1100 492" xmlns="http://www.w3.org/2000/svg">
    <defs>
      <linearGradient id="roomB" x1="0" y1="0" x2="1" y2="1">
        <stop offset="0" stop-color="#9a8a78"/>
        <stop offset="0.5" stop-color="#d8d6d2"/>
        <stop offset="1" stop-color="#7a5f48"/>
      </linearGradient>
      <linearGradient id="roomC" x1="0" y1="0" x2="1" y2="0">
        <stop offset="0" stop-color="#cfd6dc"/>
        <stop offset="0.6" stop-color="#e3e3e1"/>
        <stop offset="1" stop-color="#c4b29a"/>
      </linearGradient>
    </defs>
    <rect class="panel-bg" width="1100" height="492" fill="var(--panel-light)"/>

    <!-- upper photo band -->
    <g role="img" aria-label="Photo of a reception desk and private office workstations">
      <polygon points="440,30 1100,30 1100,177 540,177" fill="url(#roomB)"/>
    </g>
    <polygon class="accent-slash" points="374,30 440,30 540,177 485,177" fill="var(--brand-blue)"/>
    <polygon class="accent-slash" points="740,30 772,30 872,177 840,177" fill="var(--brand-blue)"/>
    <rect class="accent-bar" x="485" y="177" width="615" height="13" fill="var(--brand-blue)"/>
    <rect class="rule-bar" x="500" y="190" width="600" height="7" fill="var(--charcoal)"/>

    <!-- contact strip -->
    <text class="phone" x="586" y="252" font-size="44" fill="var(--ink)">555-014-2760</text>
    <text class="web" x="586" y="284" font-size="25" fill="var(--ink)">www.tembrolight.com</text>

    <!-- lower photo band -->
    <rect class="rule-bar" x="500" y="292" width="600" height="7" fill="var(--charcoal)"/>
    <rect class="accent-bar" x="485" y="299" width="615" height="13" fill="var(--brand-blue)"/>
    <g role="img" aria-label="Photo of an open-plan office with shared workstations and a conference table">
      <polygon points="540,312 1100,312 1100,465 440,465" fill="url(#roomC)"/>
    </g>
    <polygon class="accent-slash" points="485,312 540,312 440,465 374,465" fill="var(--brand-blue)"/>
    <polygon class="accent-slash" points="890,312 924,312 830,465 796,465" fill="var(--brand-blue)"/>

    <!-- brand block -->
    <text class="brand-name" x="28" y="228" font-size="52">TEMBROLIGHT</text>
    <text class="brand-name" x="30" y="280" font-size="34">OFFICE INTERIORS</text>
    <text class="tagline" x="30" y="330" font-size="16">Office Furniture  •  Design  •  Installation</text>
  </svg>

</main>
</body>
</html>
```